The Willow Gate: Steady Horizon

Please use the attached images as a reference and as inspiration for this contest. Please note, these images are google searched and belong to someone else.
This project is for our church.
We have a new Sermon Series launching and we want to be able to promote it and manipulate the size of the project via Facebook Cover Art, CD Labels, T-Shirts, Banners, etc.
Requesting a HD 1080 X 920 pixels.
Need an editable PSD file from the winner of the contest.
The title of the project is: Steady Horizon.
The idea behind this project is bringing things in life into focus to help our congregation be intentional about focusing on making positive changes to major areas of life.
When we think of this - we think of a camera brining something into focus to take that perfect shot, or as one of the attached images show blurry images coming into focus.
Keywords that can be used in the design are: Faith, Family, Finances, and Fitness.
Just because it is for a church does NOT mean we need it to look like its for a church. In fact, we desire the design to be compelling to someone who has never stepped foot into a church building. Avoid a "church" look.
Good Luck!
Target Market(s)
Everyone
Industry/Entity Type
House
Requirements
Must have
- Bringing "things" into focus.
- Please read description for more details
Should not have
- A church look

```html
<!DOCTYPE html>
<html lang="en">
<head>
<meta charset="utf-8">
<title>The Willow Gate: Steady Horizon</title>
<link rel="stylesheet" href="https://fonts.googleapis.com/css2?family=Questrial&family=Poiret+One&display=swap">
<style>
  :root {
    --bg-deep: #2449a0;
    --bg-mid: #2e5cb0;
    --bg-glow: #4a86b8;
    --glow-teal: #5a9aa8;
    --ring-fill: rgba(255, 255, 255, 0.07);
    --ring-edge: rgba(255, 255, 255, 0.10);
    --title-blur: rgba(235, 242, 250, 0.92);
    --title-sharp: #ffffff;
  }
  * { margin: 0; padding: 0; box-sizing: border-box; }
  html, body {
    width: 1200px;
    height: 1022px;
    overflow: hidden;
    background: var(--bg-deep);
  }
  .series-cover {
    position: relative;
    width: 1200px;
    height: 1022px;
    overflow: hidden;
    background:
      radial-gradient(ellipse 420px 380px at 620px 520px, var(--glow-teal) 0%, rgba(74,134,184,0.55) 35%, rgba(46,92,176,0) 100%),
      radial-gradient(ellipse 760px 620px at 600px 480px, var(--bg-glow) 0%, var(--bg-mid) 55%, var(--bg-deep) 100%);
  }
  .focus-rings {
    position: absolute;
    inset: 0;
  }
  .blurred-word {
    position: absolute;
    left: 0;
    width: 1200px;
    top: 268px;
    text-align: center;
    font-family: "Questrial", sans-serif;
    font-size: 250px;
    line-height: 1;
    letter-spacing: 2px;
    color: var(--title-blur);
    filter: blur(7px);
  }
  .sharp-word {
    position: absolute;
    left: 0;
    width: 1200px;
    top: 560px;
    text-align: center;
    font-family: "Poiret One", sans-serif;
    font-size: 180px;
    line-height: 1;
    letter-spacing: 14px;
    color: var(--title-sharp);
  }
  .sharp-word-trail {
    position: absolute;
    left: 0;
    width: 1200px;
    top: 580px;
    text-align: center;
    font-family: "Poiret One", sans-serif;
    font-size: 180px;
    line-height: 1;
    letter-spacing: 14px;
    color: rgba(255, 255, 255, 0.35);
    filter: blur(6px);
    transform: translateX(-14px) scaleY(1.25);
    transform-origin: 50% 0;
  }
  .sharp-word-trail.is-far {
    top: 620px;
    color: rgba(255, 255, 255, 0.14);
    filter: blur(12px);
    transform: translateX(-6px) scaleY(1.9);
  }
</style>
</head>
<body>
  <main class="series-cover">
    <svg class="focus-rings" width="1200" height="1022" viewBox="0 0 1200 1022" aria-hidden="true">
      <circle cx="200" cy="414" r="202" fill="var(--ring-fill)" stroke="var(--ring-edge)" stroke-width="1"/>
      <circle cx="467" cy="414" r="202" fill="var(--ring-fill)" stroke="var(--ring-edge)" stroke-width="1"/>
      <circle cx="728" cy="414" r="202" fill="var(--ring-fill)" stroke="var(--ring-edge)" stroke-width="1"/>
      <circle cx="1000" cy="414" r="202" fill="var(--ring-fill)" stroke="var(--ring-edge)" stroke-width="1"/>
    </svg>
    <h1 class="series-title">
      <span class="blurred-word">Steady</span>
      <span class="sharp-word-trail is-far" aria-hidden="true">Horizon</span>
      <span class="sharp-word-trail" aria-hidden="true">Horizon</span>
      <span class="sharp-word">Horizon</span>
    </h1>
  </main>
</body>
</html>
```